LED panel tester - hand-held test tool - simple label required

I have designed a product to test the LED panels of a road-side variable message sign (VMS). I don't expect to sell too many of these but thought it would look professional if it had a proper label.

I need a label designed for this hand-held test equipment. Attached is the positional layout of all the switches and text. I have also included a photo of the product.

A simple Google image search of "hand-held test tool" shows that it doesn't have to be fancy but rather functional.

I would like to put branding on the bottom 1/5th and have the option to interchange the brand if I ever get approached by one of the manufacturers of these signs. Initially it will just have a link to my website (TallowbrookWorks.com.au) right down at the bottom.

```html
<!DOCTYPE html>
<html lang="en">
<head>
<meta charset="utf-8">
<title>VMS Panel Tester – Label</title>
<link rel="stylesheet" href="https://fonts.googleapis.com/css2?family=Arimo:wght@700&display=swap">
<style>
  :root {
    --backdrop: #e8e5de;
    --label-black: #000000;
    --trace-blue: #0a64c8;
    --band-blue: #0b66c3;
    --text-white: #ffffff;
    --hole-grey: #2b2b2b;
  }
  * { box-sizing: border-box; margin: 0; padding: 0; }
  html, body {
    width: 729px;
    height: 1200px;
    overflow: hidden;
    background: var(--backdrop);
    font-family: "Arimo", Arial, sans-serif;
  }
  .label {
    position: absolute;
    left: 100px;
    top: 20px;
    width: 528px;
    height: 1160px;
    background: var(--label-black);
    overflow: hidden;
  }
  .title-band {
    position: absolute;
    left: 0; top: 0;
    width: 100%; height: 76px;
    background: var(--band-blue);
    color: var(--text-white);
    font-size: 35px;
    font-weight: 700;
    letter-spacing: 0.3px;
    display: flex;
    align-items: center;
    justify-content: center;
  }
  .trace-field {
    position: absolute;
    left: 0; top: 76px;
    width: 100%; height: 1023px;
    background:
      radial-gradient(ellipse 60% 45% at 50% 40%, rgba(10,100,200,0.22), rgba(10,100,200,0) 70%),
      linear-gradient(180deg, #000 0%, #03101f 55%, #06234a 100%);
  }
  .brand-band {
    position: absolute;
    left: 0; bottom: 0;
    width: 100%; height: 61px;
    background: var(--band-blue);
    color: var(--text-white);
    font-size: 27px;
    font-weight: 700;
    display: flex;
    align-items: center;
    justify-content: center;
  }
  .switch-ring {
    position: absolute;
    width: 68px; height: 68px;
    border: 3px solid var(--trace-blue);
    border-radius: 50%;
    background: var(--label-black);
    display: flex;
    align-items: center;
    justify-content: center;
  }
  .switch-ring::after {
    content: "";
    width: 30px; height: 30px;
    border-radius: 50%;
    background: var(--hole-grey);
  }
  .tag {
    position: absolute;
    height: 40px;
    border: 3px solid var(--trace-blue);
    border-radius: 20px;
    background: var(--label-black);
    color: var(--text-white);
    font-size: 22px;
    font-weight: 700;
    display: flex;
    align-items: center;
    justify-content: center;
  }
  .rocker-window {
    position: absolute;
    left: 147px; top: 695px;
    width: 234px; height: 161px;
    border: 3px solid var(--trace-blue);
    background: var(--label-black);
  }
  .power-led {
    position: absolute;
    left: 417px; top: 694px;
    width: 48px; height: 48px;
    border: 3px solid var(--trace-blue);
    border-radius: 50%;
    background: var(--label-black);
  }
</style>
</head>
<body>
  <div class="label">
    <div class="title-band">VMS PANEL TESTER</div>

    <div class="trace-field" role="img" aria-label="Blue circuit-board trace pattern on black"></div>

    <div class="switch-ring" style="left:230px; top:183px;"></div>
    <div class="switch-ring" style="left:230px; top:260px;"></div>
    <div class="switch-ring" style="left:230px; top:336px;"></div>
    <div class="switch-ring" style="left:230px; top:413px;"></div>
    <div class="switch-ring" style="left:230px; top:490px;"></div>
    <div class="switch-ring" style="left:230px; top:567px;"></div>

    <div class="tag" style="left:325px; top:197px; width:82px;">RED</div>
    <div class="tag" style="left:325px; top:274px; width:119px;">GREEN</div>
    <div class="tag" style="left:325px; top:350px; width:137px;">ORANGE</div>
    <div class="tag" style="left:325px; top:427px; width:112px;">WHITE</div>
    <div class="tag" style="left:325px; top:504px; width:93px;">BLUE</div>
    <div class="tag" style="left:325px; top:581px; width:102px;">SLOW</div>
    <div class="tag" style="left:105px; top:581px; width:99px;">FAST</div>

    <div class="rocker-window"></div>

    <div class="power-led"></div>
    <div class="tag" style="left:390px; top:758px; width:102px; height:37px; font-size:21px;">POWER</div>

    <div class="brand-band">www.TallowbrookWorks.com.au</div>
  </div>
</body>
</html>
```